business card design - photography

I am a fine art photographer. I would like to approach galleries to exhibit my work and need a business card.

The card should convey creativity and simplicity.
I would like a double sided card.

Some options:
1. An all white card with raised or embossed text or design to create a tactile finish.
2. a white and dark grey design would also work well.
3. Would be great to use my name as part of the design but not essential.
4. My name and title on the front, other details on the back of card.

The final design should be simple, minimal, elegant and innovative.
Being minimal, it will be more about texture, text size and placement.

examples of designs I would prefer provided here:
http://plimvarka.com/ideas/40-quiet-and-refined-card-layouts

I'm also open to other designs that may be unusual and unique.

Love this:
http://www.snapvelo.com/pics/morningverselog/583014927
Updates

I have uploaded a psd file after playing around in photoshop with various fonts.  I like the font (which I downloaded from glyphmorra.com called Arual) but the design probably needs some refining.  I hope this helps.  If you'd like me to change the format of the file, please let me know.

Ilvane

Target Market(s)

Art Gallery owners/administrators and customers.

Industry/Entity Type

Business

Requirements
Must have
• A unique look.

Matte, silky finish or heavy textured stock. Double-sided card.

Front:
my name
photography by

Back:
phone no
email
web address
Nice to have
• Letterpress
embrossed
Clean fonts
Should not have
• Do not use illustrations of cameras or lenses.
No frames around the card edge.

```html
<!DOCTYPE html>
<html lang="en">
<head>
<meta charset="utf-8">
<title>Photography by Ilvane Marrow — Business Card</title>
<link rel="stylesheet" href="https://fonts.googleapis.com/css2?family=Montserrat:wght@400;700&family=Open+Sans:wght@700&family=PT+Sans:wght@400&display=swap">
<style>
  :root {
    --card-dark: #0d0d0d;
    --card-mid: #1c1c1c;
    --gap-white: #ffffff;
    --silver-light: #f0f0f0;
    --silver-mid: #d2d2d2;
    --silver-dark: #a9a9a9;
    --ink: #111111;
    --ink-soft: #3a3a3a;
  }
  * { margin: 0; padding: 0; box-sizing: border-box; }
  html, body {
    width: 984px; height: 1200px; overflow: hidden;
    background: var(--gap-white);
  }
  .canvas { position: relative; width: 984px; height: 1200px; }

  .card {
    position: absolute; left: 0; width: 984px;
    background:
      radial-gradient(ellipse 70% 60% at 50% 50%, var(--card-mid), transparent 75%),
      linear-gradient(180deg, var(--card-dark), #161616 50%, var(--card-dark));
    overflow: hidden;
  }
  .card--front { top: 0; height: 601px; width: 981px; }
  .card--back { top: 612px; height: 588px; }

  .silver-plate {
    position: absolute;
    background: linear-gradient(100deg, var(--silver-dark) 0%, var(--silver-mid) 20%, var(--silver-light) 55%, var(--silver-mid) 80%, var(--silver-dark) 100%);
  }
  .card--front .silver-plate { left: 0; top: 184px; width: 544px; height: 211px; }
  .card--back .silver-plate { left: 0; top: 189px; width: 984px; height: 210px; }

  .title-line {
    position: absolute; left: 19px; top: 38px;
    font-family: "Montserrat", sans-serif; font-weight: 700;
    font-size: 17px; letter-spacing: 0.5px; color: var(--ink);
  }
  .name-line {
    position: absolute; left: 38px; top: 84px;
    font-family: "Montserrat", sans-serif; font-weight: 400;
    font-size: 58px; line-height: 1; color: var(--ink-soft);
    white-space: nowrap;
  }

  .contact { position: absolute; left: 0; top: 0; width: 984px; height: 210px; color: var(--ink); white-space: nowrap; line-height: 1; }
  .contact__label {
    position: absolute;
    font-family: "PT Sans", sans-serif; font-weight: 400;
    font-size: 38px; letter-spacing: -1px;
  }
  .contact__value {
    position: absolute;
    font-family: "Open Sans", sans-serif; font-weight: 700;
    font-size: 39px; letter-spacing: -1.2px;
  }
  .row-email { top: 36px; }
  .row-number { top: 76px; }
  .row-website { top: 116px; }
</style>
</head>
<body>
<div class="canvas">
  <section class="card card--front">
    <div class="silver-plate">
      <p class="title-line">PHOTOGRAPHY BY</p>
      <p class="name-line">Ilvane Marrow</p>
    </div>
  </section>

  <section class="card card--back">
    <div class="silver-plate">
      <div class="contact">
        <span class="contact__label row-email" style="left:97px;">EMAIL</span>
        <span class="contact__value row-email" style="left:334px;top:31px;">IMARROW@POSTMAIL.COM</span>
        <span class="contact__label row-number" style="left:169px;">NUMBER</span>
        <span class="contact__value row-number" style="left:406px;top:71px;">0412 578 903</span>
        <span class="contact__label row-website" style="left:101px;">WEBSITE</span>
        <span class="contact__value row-website" style="left:337px;top:111px;">WWW.ILVANEMARROW.COM</span>
      </div>
    </div>
  </section>
</div>
</body>
</html>
```